My friend is opening up a tool shop and I want to make him a flyer to pass out to the neighborhood. The name of his shop is "Cousin Walt's Tool Shop" . He is a dealer for Brightforge tools http://www.brightforgetools-example.net/ The business address is:

2741 N Birch Avenue
Oakridge Park, WI 60893

He's basically selling hand tools, power tools, cutting glass, cutting keys. He has no logo, but if one is incorporated on this, that would gain your design brownie points.

```html
<!DOCTYPE html>
<html lang="en">
<head>
<meta charset="utf-8">
<title>Cousin Walt's Tool Shop</title>
<link rel="stylesheet" href="https://fonts.googleapis.com/css2?family=Alfa+Slab+One&family=Montserrat:wght@400;500&display=swap">
<style>
  :root {
    --shop-red: #d2232a;
    --paper: #ffffff;
    --ink: #1f1f1f;
    --shadow: #3a1213;
    --steel-light: #f1f1f1;
    --steel-dark: #bdbdbd;
    --steel-edge: #9a9a9a;
    --brand-navy: #1d2f7a;
  }
  html, body { margin: 0; padding: 0; overflow: hidden; }
  body { width: 845px; height: 1200px; }
  .flyer {
    position: relative;
    width: 845px; height: 1200px;
    background: var(--shop-red);
    font-family: "Montserrat", sans-serif;
    color: var(--paper);
    overflow: hidden;
  }
  .shop-name {
    position: absolute; top: 78px; left: 0; width: 100%;
    margin: 0; text-align: center;
    font-family: "Alfa Slab One", serif; font-weight: 400;
    font-size: 118px; line-height: 156px; letter-spacing: 2px;
    color: var(--paper);
    text-shadow: 6px 6px 0 var(--shadow);
  }
  .shop-type {
    position: absolute; top: 400px; left: 0; width: 100%;
    display: flex; justify-content: center; align-items: center; gap: 22px;
    font-size: 44px; font-weight: 400; letter-spacing: 2px;
  }
  .dealer-label {
    position: absolute; top: 520px; left: 0; width: 100%; margin: 0;
    text-align: center; font-size: 21px; font-weight: 500; letter-spacing: 0.5px;
  }
  .dealer-badge {
    position: absolute; left: 196px; top: 562px; width: 438px; height: 124px;
    box-sizing: border-box; border-radius: 10px;
    border: 4px solid var(--steel-edge);
    background: linear-gradient(180deg, var(--steel-light), var(--steel-dark));
    display: flex; align-items: center; justify-content: center; gap: 16px;
  }
  .dealer-badge .mark {
    flex: none; width: 34px; height: 34px; background: var(--brand-navy);
  }
  .dealer-badge .brand {
    font-size: 40px; font-weight: 500; color: var(--brand-navy); letter-spacing: 1px;
  }
  .services {
    position: absolute; top: 718px; left: 128px; width: 600px;
    display: grid; grid-template-columns: 290px 310px; row-gap: 10px;
    margin: 0; padding: 0; list-style: none;
    font-size: 31px; font-weight: 400;
  }
  .services li { display: flex; align-items: center; gap: 10px; white-space: nowrap; }
  .services li:nth-child(3) { margin-left: -18px; }
  .tools-art {
    position: absolute; left: 40px; top: 850px; width: 780px; height: 190px;
    background: linear-gradient(180deg, rgba(255,255,255,0.15), rgba(255,255,255,0.9));
  }
  .contact-band {
    position: absolute; left: 0; top: 1038px; width: 845px; height: 162px;
    background: var(--paper); color: var(--ink);
  }
  .address {
    position: absolute; left: 52px; top: 60px; margin: 0;
    font-style: normal; font-size: 21px; line-height: 30px;
  }
  .call-label {
    position: absolute; left: 484px; top: 18px;
    font-size: 31px; font-weight: 500; color: var(--shop-red); letter-spacing: 1px;
  }
  .phone {
    position: absolute; left: 392px; top: 56px;
    font-size: 55px; font-weight: 500; color: var(--ink); letter-spacing: 1px;
  }
  .bullet { flex: none; }
</style>
</head>
<body>
<main class="flyer">
  <h1 class="shop-name">COUSIN<br>WALT'S</h1>

  <div class="shop-type">
    <svg class="bullet" width="20" height="20" viewBox="0 0 20 20" aria-hidden="true"><circle cx="10" cy="10" r="9" fill="#fff"/><line x1="5" y1="15" x2="15" y2="5" stroke="#d2232a" stroke-width="2.5"/></svg>
    <span>TOOL SHOP</span>
    <svg class="bullet" width="20" height="20" viewBox="0 0 20 20" aria-hidden="true"><circle cx="10" cy="10" r="9" fill="#fff"/><line x1="5" y1="15" x2="15" y2="5" stroke="#d2232a" stroke-width="2.5"/></svg>
  </div>

  <p class="dealer-label">AUTHORIZED DEALER FOR</p>
  <div class="dealer-badge">
    <span class="mark"></span>
    <span class="brand">BRIGHTFORGE</span>
  </div>

  <ul class="services">
    <li><svg class="bullet" width="18" height="18" viewBox="0 0 20 20" aria-hidden="true"><circle cx="10" cy="10" r="9" fill="#fff"/><line x1="5" y1="15" x2="15" y2="5" stroke="#d2232a" stroke-width="2.5"/></svg>HAND TOOLS</li>
    <li><svg class="bullet" width="18" height="18" viewBox="0 0 20 20" aria-hidden="true"><circle cx="10" cy="10" r="9" fill="#fff"/><line x1="5" y1="15" x2="15" y2="5" stroke="#d2232a" stroke-width="2.5"/></svg>POWER TOOLS</li>
    <li><svg class="bullet" width="18" height="18" viewBox="0 0 20 20" aria-hidden="true"><circle cx="10" cy="10" r="9" fill="#fff"/><line x1="5" y1="15" x2="15" y2="5" stroke="#d2232a" stroke-width="2.5"/></svg>CUTTING GLASS</li>
    <li><svg class="bullet" width="18" height="18" viewBox="0 0 20 20" aria-hidden="true"><circle cx="10" cy="10" r="9" fill="#fff"/><line x1="5" y1="15" x2="15" y2="5" stroke="#d2232a" stroke-width="2.5"/></svg>CUTTING KEYS</li>
  </ul>

  <div class="tools-art" role="img" aria-label="White silhouettes of a row of tools: drill, scissors, pliers, wrench, screwdrivers, spanner, trowel and hammer"></div>

  <footer class="contact-band">
    <address class="address">2741 N Birch Avenue<br>Oakridge Park, WI 60893</address>
    <div class="call-label">CALL US NOW</div>
    <div class="phone">(555)555-0142</div>
  </footer>
</main>
</body>
</html>
```